Etiketten für Kuchen im Glas
Zielgruppe
Die Firma Wefrat bietet kulinarische Präsente und Geschenkideen zum Thema kreatives Backen an. Unsere Zielgruppe ist B2C und Werbetreibende, die unsere Produkte als Geschenke einsetzen.
Aufgabenstellung
Für unsere Zielgruppe "Feinkostläden" benötigen wir ein etwas edleres klasssisches Etiketten-Design.
Gestaltet wird der Deckel und die Vorderseite eines Etiketts für ein 290 ml PLUVE-Glas. Die entsprechende Designvorlage steht hier zum Download bereit:
https://files.kastenwolke-beispiel.de/u/4827153/3518_06274_0000-Vorlage%20CMYK%20v08_2013-09.psd
Benötigt werden 4 unterschiedliche Etiketten, die aber aus einem "Guss" sein sollten für die Sorten: Stracciatella, Schokolade, Zitrone, Stollen. Die Sorte sollte mit auf dem Etikett stehen.
Sonstige Angaben auf dem Etikett:
- optional "Kuchen im Glas"
- gerne Grünhof Logo (siehe Anhang)
- optional "fertig gebacken". Könnte z.B. gut auf dem Deckel in Kombination mit "Kuchen im Gla" stehen
Achtung: Das Etikett für die Rückseite mit Deklaration muss nicht gestaltet werden.
Tipps: Das Etikett ist konisch und das Glas rund. Das bedeutet, dass Bilder + Schriften mit einer leichten Wölbung kreiert werden sollten. Für die Wölbung kann man sich gut an der unteren Designlinie orientieren.
Farbgestaltung: eher dunkel; z.B. Grau, Dunkelblau evtl. Schwarz
Schriften: Es dürfen auch kostenpflichtige Schriften verwendet werden. Freie Schriften allerdings bevorzugt
Format: Photoshop PSD inklusive allen Ebenen und verwendeten Elementen als einzelne Ebene.
Bei Fragen gerne melden, ich freue mich auf Eure Designs.

```html
<!DOCTYPE html>
<html lang="de">
<head>
<meta charset="utf-8">
<title>Kuchen im Glas – Zitrone</title>
<link rel="stylesheet" href="https://fonts.googleapis.com/css2?family=Cinzel:wght@500&family=Pinyon+Script&display=swap">
<style>
  :root {
    --bg: #f4f4f2;
    --grey-dark: #6f7073;
    --grey-mid: #9c9da0;
    --grey-light: #c9cacc;
    --cream: #fcf8e8;
    --gold: #c9a53c;
    --gold-deep: #a9861f;
    --navy: #26285e;
    --ink: #4a4a4d;
    --white: #ffffff;
    --lemon: #f2d43a;
    --leaf: #3f7a2c;
  }
  * { box-sizing: border-box; margin: 0; padding: 0; }
  html, body { width: 1104px; height: 1200px; overflow: hidden; }
  body { background: var(--bg); position: relative; }

  .lid-label {
    position: absolute; left: 327px; top: 40px;
    width: 450px; height: 450px; border-radius: 50%;
    background: radial-gradient(circle at 50% 45%, var(--grey-light), var(--grey-mid) 60%, var(--grey-dark));
    border: 4px solid var(--grey-dark);
    box-shadow: inset 0 0 0 10px rgba(255,255,255,0.25);
  }
  .front-label {
    position: absolute; left: 72px; top: 560px;
    width: 960px; height: 580px;
    background: linear-gradient(180deg, var(--grey-mid), var(--grey-light) 45%, var(--grey-mid));
    border-top: 3px solid var(--grey-dark);
    border-radius: 0 0 50% 50% / 0 0 48px 48px;
  }
  .plaque {
    position: absolute; left: 50%; transform: translateX(-50%);
    background: var(--cream);
    border: 3px solid var(--gold);
    border-radius: 28px;
    box-shadow: inset 0 0 0 6px var(--cream), inset 0 0 0 8px var(--gold-deep), 0 4px 10px rgba(0,0,0,0.25);
    text-align: center;
  }
  .lid-label .plaque { top: 108px; width: 330px; height: 170px; }
  .front-label .plaque { top: 100px; width: 560px; height: 290px; }

  .tagline {
    font-family: "Cinzel", serif; font-weight: 500;
    color: var(--ink); letter-spacing: 0.12em;
  }
  .lid-label .tagline { font-size: 13px; margin-top: 18px; }
  .front-label .tagline { font-size: 22px; margin-top: 30px; }

  .product-name {
    font-family: "Pinyon Script", cursive; color: var(--navy); line-height: 1;
  }
  .lid-label .product-name { font-size: 46px; margin-top: 6px; }
  .front-label .product-name { font-size: 80px; margin-top: 10px; }

  .lemon-art {
    display: block; margin: 0 auto; border-radius: 50%;
    background: radial-gradient(circle at 40% 40%, var(--lemon), #d9b520 60%, var(--leaf));
  }
  .lid-label .lemon-art { width: 54px; height: 32px; margin-top: 10px; }
  .front-label .lemon-art { width: 96px; height: 56px; margin-top: 20px; }

  .flavour {
    position: absolute; left: 0; width: 100%; text-align: center;
    font-family: "Pinyon Script", cursive; color: var(--white);
    text-shadow: 0 2px 3px rgba(0,0,0,0.35);
  }
  .lid-label .flavour { top: 300px; font-size: 48px; }
  .front-label .flavour { top: 430px; font-size: 70px; }

  .pattern-area {
    position: absolute; inset: 0; border-radius: inherit;
    background: linear-gradient(135deg, rgba(255,255,255,0.12), rgba(0,0,0,0.06));
  }
</style>
</head>
<body>
  <section class="lid-label">
    <div class="pattern-area" role="img" aria-label="Graues Rautenmuster im Hintergrund"></div>
    <div class="plaque">
      <p class="tagline">– FERTIG GEBACKEN –</p>
      <h1 class="product-name">Kuchen im Glas</h1>
      <span class="lemon-art" role="img" aria-label="Zitronen mit Blättern"></span>
    </div>
    <p class="flavour">Zitrone</p>
  </section>

  <section class="front-label">
    <div class="pattern-area" role="img" aria-label="Graues Rautenmuster im Hintergrund"></div>
    <div class="plaque">
      <p class="tagline">– FERTIG GEBACKEN –</p>
      <h2 class="product-name">Kuchen im Glas</h2>
      <span class="lemon-art" role="img" aria-label="Zitronen mit Blättern"></span>
    </div>
    <p class="flavour">Zitrone</p>
  </section>
</body>
</html>
```